Apartments rental business needs a web for direct reservations.

I need a website that allows my clients to check the property (pictures, a brief description etc) and lets them make reservations. They will be providing the required information such as name, last name, email address and credit card details. Also a calendar where I can update the availability (dates and prices) of the property upon new reservations is a must. I already have a logo that should also be a good starting point for colors, style an inspiration.

Need extra days to review

```html
<!DOCTYPE html>
<html lang="en">
<head>
<meta charset="utf-8">
<title>Harbourlane – Reservations</title>
<link href="https://fonts.googleapis.com/css2?family=Montserrat:wght@400;600;700;800&family=Open+Sans:wght@400;600&display=swap" rel="stylesheet">
<style>
:root{
  --teal:#1fa597;
  --teal-dark:#178a7e;
  --forest:#1c3a35;
  --forest-deep:#132a26;
  --orange:#f06a2c;
  --orange-dark:#7a3416;
  --ink:#1b1b1b;
  --muted:#777;
  --paper:#ffffff;
  --soft:#f4f4f4;
}
*{box-sizing:border-box;margin:0;padding:0}
html,body{width:1200px;height:5070px;overflow:hidden}
body{font-family:"Open Sans",sans-serif;color:var(--ink);background:var(--paper);position:relative}
h1,h2,h3,h4,.btn,.nav a,.brand{font-family:"Montserrat",sans-serif}
section,header,footer{position:absolute;left:0;width:1200px}
.btn{display:inline-block;background:var(--teal);color:#fff;font-size:15px;font-weight:600;padding:13px 34px;text-decoration:none}
.photo{position:absolute}

/* header + hero */
.hero{top:0;height:640px;background:var(--paper)}
.brand{position:absolute;left:34px;top:14px;display:flex;align-items:center;gap:8px;color:var(--orange);font-weight:700;font-size:17px}
.brand .dot{width:24px;height:24px;border-radius:50%;background:var(--orange)}
.nav{position:absolute;left:585px;top:19px;display:flex;gap:34px;z-index:2}
.nav a{font-size:12px;color:#333;text-decoration:none;white-space:nowrap}
.social{position:absolute;left:1015px;top:17px;display:flex;gap:7px}
.social span{width:16px;height:16px;background:var(--teal);display:block}
.hero-img{left:405px;top:60px;width:795px;height:580px;background:linear-gradient(160deg,#cfe3ef 0%,#e9ecef 35%,#b9c3c1 55%,#6d8a4c 85%,#4f6e34 100%)}
.hero-shape{position:absolute;left:380px;top:55px}
.hero-kicker{position:absolute;left:95px;top:330px;font-size:19px;font-weight:600;color:var(--forest)}
.hero-title{position:absolute;left:93px;top:352px;font-size:62px;font-weight:800;color:var(--forest-deep)}
.hero .btn{position:absolute;left:95px;top:440px}

/* about */
.about{top:640px;height:595px;background:var(--paper)}
.about-frame{position:absolute;left:125px;top:75px;width:450px;height:410px;border:12px solid var(--teal)}
.about-img{left:140px;top:92px;width:400px;height:385px;background:linear-gradient(180deg,#e4e2df 0%,#d3cfca 55%,#8e2a2a 70%,#c9c6c2 100%)}
.about-text{position:absolute;left:632px;top:115px;width:470px}
.kicker{color:var(--orange);font-size:15px;font-weight:600;letter-spacing:.5px;font-family:"Montserrat",sans-serif}
.about-text h2{font-size:31px;font-weight:800;line-height:1.2;margin:8px 0 14px;color:var(--ink)}
.about-text p{font-size:12.5px;line-height:1.55;color:var(--muted);margin-bottom:12px}
.about-text .btn{margin-top:14px}

/* services */
.services{top:1235px;height:651px;background:var(--forest)}
.services .kicker{position:absolute;left:95px;top:68px;color:#d9e3e1;font-weight:400;font-size:14px}
.services h2{position:absolute;left:95px;top:88px;color:#fff;font-size:30px;font-weight:800}
.service{position:absolute;width:320px;height:200px;background:rgba(255,255,255,.09);border:1px solid rgba(255,255,255,.18);display:flex;flex-direction:column;align-items:center;justify-content:center;gap:22px;color:#fff;font-family:"Montserrat",sans-serif;font-size:17px;font-weight:600}
.service.active{background:var(--orange);border-color:var(--orange)}

/* pricing */
.pricing{top:1886px;height:767px;background:var(--paper);text-align:center}
.pricing h2{position:absolute;width:100%;top:62px;font-size:32px;font-weight:800}
.pricing .sub{position:absolute;width:100%;top:100px;font-size:21px;font-family:"Montserrat",sans-serif}
.plan{position:absolute;top:160px;width:320px;height:530px;background:var(--teal);color:#fff}
.plan .photo{position:relative;height:193px;width:100%}
.plan ul{list-style:none;padding:18px 38px 0}
.plan li{font-size:16px;padding:10px 0;border-bottom:1px solid rgba(255,255,255,.45)}
.plan li:last-child{border:none}
.plan .book{position:absolute;bottom:0;left:0;width:100%;height:52px;line-height:52px;background:var(--forest-deep);font-family:"Montserrat",sans-serif;font-weight:600;font-size:16px}
.plan.featured{background:var(--orange)}
.plan.featured .book{background:var(--orange-dark)}

/* feedback */
.feedback{top:2653px;height:440px;background:linear-gradient(90deg,#1a3531,#223f3a 60%,#1a3531)}
.feedback h2{position:absolute;left:95px;top:150px;color:#fff;font-size:32px;font-weight:800}
.feedback .intro{position:absolute;left:95px;top:198px;width:370px;color:#c9d4d2;font-size:12px;line-height:1.5}
.quote{position:absolute;top:80px;width:270px;height:275px;border:1px solid rgba(255,255,255,.25);background:rgba(255,255,255,.04);text-align:center;color:#dbe4e2}
.quote .avatar{width:70px;height:70px;border-radius:50%;margin:40px auto 14px}
.quote p{font-size:12px;line-height:1.45;padding:0 30px}
.quote h4{color:#fff;font-size:18px;font-weight:600;margin-top:14px}
.quote small{font-size:12px}
.dots{position:absolute;right:14px;top:195px;display:flex;flex-direction:column;gap:10px}
.dots i{width:8px;height:8px;border-radius:50%;background:#fff;display:block}
.dots i:first-child{background:var(--orange)}

/* news */
.news{top:3093px;height:591px;background:var(--paper)}
.news h2{position:absolute;width:100%;text-align:center;top:62px;font-size:34px;font-weight:800}
.post{position:absolute;top:125px;width:320px;height:416px;background:#fff;box-shadow:0 0 10px rgba(0,0,0,.12)}
.post .photo{position:absolute;left:0;width:320px;height:208px}
.post .body{position:absolute;left:0;width:320px;padding:16px 24px}
.post .date{color:var(--orange);font-size:13px;font-weight:600}
.post h3{font-size:19px;font-weight:700;margin:2px 0 6px}
.post p{font-size:12px;color:var(--muted);line-height:1.45}
.post .btn{font-size:11px;padding:6px 14px;margin-top:12px}

/* gallery */
.gallery{top:3684px;height:490px;background:var(--paper)}
.gallery h2{position:absolute;width:100%;text-align:center;top:52px;font-size:33px;font-weight:800}

/* contact */
.contact{top:4174px;height:474px}
.map{left:0;top:0;width:602px;height:474px;background:linear-gradient(135deg,#e8ebe6,#dfe6ea 50%,#e9ece4)}
.contact-form{position:absolute;left:602px;top:0;width:598px;height:474px;background:var(--teal);padding:125px 95px 0 80px}
.field{color:#fff;font-size:12px;border-bottom:1px solid rgba(255,255,255,.75);padding-bottom:10px;margin-bottom:40px}
.field.message{margin-bottom:52px}
.contact-form .submit{display:inline-block;border:1px solid #fff;color:#fff;font-family:"Montserrat",sans-serif;font-size:14px;padding:8px 26px}

/* footer */
.footer{top:4648px;height:422px;background:var(--forest-deep);color:#c9d2d0}
.footer h4{color:#fff;font-size:19px;font-weight:600;margin-bottom:18px}
.fcol{position:absolute;top:75px;font-size:12px;line-height:2}
.fcol ul{list-style:none}
.feed{display:grid;grid-template-columns:repeat(3,72px);gap:5px}
.feed span{height:46px;display:block}
.news-form{display:flex;margin-top:12px}
.news-form span{width:150px;height:26px;background:#fff;color:#999;font-size:10px;padding:4px 8px;line-height:18px}
.news-form b{width:78px;height:26px;background:var(--forest-deep);border:1px solid #fff;color:#fff;font-size:11px;text-align:center;line-height:24px}
.footer-brand{position:absolute;left:0;width:100%;top:255px;display:flex;justify-content:center;align-items:center;gap:8px;color:var(--orange);font-family:"Montserrat",sans-serif;font-weight:700;font-size:17px}
.footer-brand .dot{width:24px;height:24px;border-radius:50%;background:var(--orange)}
.copyright{position:absolute;width:100%;top:300px;text-align:center;font-size:11px}
.copyright b{color:var(--orange)}
</style>
</head>
<body>

<header class="hero">
  <div class="brand"><span class="dot"></span>HARBOURLANE</div>
  <nav class="nav"><a href="#">Home</a><a href="#">About us</a><a href="#">Properties</a><a href="#">Blog</a><a href="#">Contact</a></nav>
  <div class="social"><span></span><span></span><span></span><span></span></div>
  <div class="photo hero-img" role="img" aria-label="Photo of a white holiday apartment with a terrace and sun loungers"></div>
  <svg class="hero-shape" width="200" height="590" viewBox="0 0 200 590">
    <polygon points="0,0 110,0 165,110 40,0" fill="var(--teal)"/>
    <polygon points="25,0 120,0 200,210 200,590 180,590" fill="#fff"/>
    <polygon points="5,0 30,0 185,590 160,590" fill="var(--teal)"/>
  </svg>
  <p class="hero-kicker">ARE YOU LOOKING FOR A PLACE TO</p>
  <h1 class="hero-title">Reservations</h1>
  <a class="btn" href="#">Book Now</a>
</header>

<section class="about">
  <div class="about-frame"></div>
  <div class="photo about-img" role="img" aria-label="Photo of a bright living room with a red sofa and framed line art"></div>
  <div class="about-text">
    <p class="kicker">ABOUT OUR COMPANY</p>
    <h2>ARE YOU LOOKING FOR<br>A PLACE TO RESERVATIONS</h2>
    <p>Our apartments sit a short walk from the beach, each one cleaned, checked and ready before you arrive. Book direct with us and enjoy the best available rate, quick replies and a warm welcome at the door.</p>
    <p>Every stay includes fresh linen, fast wifi and a local guide to the town. Pick your dates, choose your apartment and confirm in minutes.</p>
    <a class="btn" href="#">Know More</a>
  </div>
</section>

<section class="services">
  <p class="kicker">OUR ALL SERVICES</p>
  <h2>WHY WE ARE THE BEST</h2>
  <div class="service" style="left:95px;top:157px">
    <svg width="40" height="40" viewBox="0 0 40 40" fill="none" stroke="#fff" stroke-width="2"><rect x="6" y="6" width="28" height="28"/><path d="M13 26v-8l7-6 7 6v8z"/></svg>EXPERT TECHNICIANS</div>
  <div class="service active" style="left:440px;top:157px">
    <svg width="40" height="40" viewBox="0 0 40 40" fill="none" stroke="#fff" stroke-width="2"><path d="M6 20L20 7l14 13M10 17v17h20V17"/><circle cx="20" cy="24" r="4"/></svg>JUST YOU &amp; NATURE</div>
  <div class="service" style="left:788px;top:157px">
    <svg width="40" height="40" viewBox="0 0 40 40" fill="none" stroke="#fff" stroke-width="2"><rect x="9" y="5" width="20" height="28"/><path d="M13 12h12M13 18h12M13 24h7"/><path d="M26 26l4 4 6-8"/></svg>HIGHLY RECOMENDED</div>
  <div class="service" style="left:95px;top:381px">
    <svg width="40" height="40" viewBox="0 0 40 40" fill="none" stroke="#fff" stroke-width="2"><path d="M4 34h32M8 34V16l12-9 12 9v18M16 34v-9h8v9"/></svg>IN THE BEST LOCALE</div>
  <div class="service" style="left:440px;top:381px">
    <svg width="40" height="40" viewBox="0 0 40 40" fill="none" stroke="#fff" stroke-width="2"><rect x="6" y="5" width="18" height="24"/><path d="M10 12h10M10 18h10"/><circle cx="28" cy="27" r="7"/><path d="M25 27l2 2 4-4"/></svg>POSITIVE REVIEWS</div>
  <div class="service" style="left:788px;top:381px">
    <svg width="40" height="40" viewBox="0 0 40 40" fill="none" stroke="#fff" stroke-width="2"><path d="M20 6l8 8-8 8-8-8z"/><path d="M6 34c4-8 8-8 14-8s10 0 14 8"/></svg>EASY RESERVATION</div>
</section>

<section class="pricing">
  <h2>OUR PRICING</h2>
  <p class="sub">View To Our Great Resort</p>
  <div class="plan" style="left:95px">
    <div class="photo" role="img" aria-label="Photo of a dining area with red chairs" style="background:linear-gradient(180deg,#e3e1de,#b9b2ab 60%,#9a3b31)"></div>
    <ul><li>CLASSIC</li><li>2 beds in room</li><li>4 people in room</li><li>1200 sqf</li><li>Split AC</li><li>Starts From $60.00 / Night</li></ul>
    <div class="book">Book Now</div>
  </div>
  <div class="plan featured" style="left:440px">
    <div class="photo" role="img" aria-label="Photo of a bedroom with blue towels on the bed" style="background:linear-gradient(180deg,#e7e7ea,#cfd2d8 55%,#2c3e75)"></div>
    <ul><li>CLASSIC</li><li>2 beds in room</li><li>4 people in room</li><li>1200 sqf</li><li>Split AC</li><li>Starts From $60.00 / Night</li></ul>
    <div class="book">Book Now</div>
  </div>
  <div class="plan" style="left:788px">
    <div class="photo" role="img" aria-label="Photo of a kitchen with dark worktops" style="background:linear-gradient(180deg,#eef0f1,#c9cdd0 60%,#3b3f42)"></div>
    <ul><li>CLASSIC</li><li>2 beds in room</li><li>4 people in room</li><li>1200 sqf</li><li>Split AC</li><li>Starts From $60.00 / Night</li></ul>
    <div class="book">Book Now</div>
  </div>
</section>

<section class="feedback">
  <h2>CLIENT’S FEEDBACK</h2>
  <p class="intro">Guests return every season for the quiet streets, the sea view and the easy booking. Here is what a few of them told us after their stay with Harbourlane.</p>
  <div class="quote" style="left:530px">
    <div class="avatar" role="img" aria-label="Guest portrait" style="background:#6b5a4e"></div>
    <p>Clean rooms, a calm terrace and a host who answered every message within minutes.</p>
    <h4>Carlos Doe</h4><small>Ceo of Loren</small>
  </div>
  <div class="quote" style="left:832px">
    <div class="avatar" role="img" aria-label="Guest portrait" style="background:#c9b49a"></div>
    <p>Booking direct was quick and the apartment looked exactly like the photos.</p>
    <h4>Carlos Doe</h4><small>Ceo of Loren</small>
  </div>
  <div class="dots"><i></i><i></i><i></i></div>
</section>

<section class="news">
  <h2>OUR LATEST NEWS</h2>
  <article class="post" style="left:95px">
    <div class="photo" role="img" aria-label="Photo of a terrace with sun loungers" style="top:0;background:linear-gradient(180deg,#9fb9c9,#7d8a6a 55%,#3c3a38)"></div>
    <div class="body" style="top:208px"><p class="date">18 April</p><h3>Lorem Ipsam Enim</h3><p>New terrace loungers are in place for the summer season at every apartment.</p><a class="btn" href="#">Read More</a></div>
  </article>
  <article class="post" style="left:440px">
    <div class="body" style="top:0"><p class="date">18 April</p><h3>Lorem Ipsam Enim</h3><p>Late check-out is now free on Sundays for all direct bookings.</p><a class="btn" href="#">Read More</a></div>
    <div class="photo" role="img" aria-label="Photo of a living room with framed art" style="top:208px;background:linear-gradient(180deg,#e2e0dd,#bdb7b1 60%,#8c2a2a)"></div>
  </article>
  <article class="post" style="left:788px">
    <div class="photo" role="img" aria-label="Photo of a white kitchen" style="top:0;background:linear-gradient(180deg,#f0f1f2,#cfd3d5 60%,#4a4e51)"></div>
    <div class="body" style="top:208px"><p class="date">18 April</p><h3>Lorem Ipsam Enim</h3><p>Every kitchen now has a coffee maker and a welcome pack on arrival.</p><a class="btn" href="#">Read More</a></div>
  </article>
</section>

<section class="gallery">
  <h2>OUR GALLERY</h2>
  <div class="photo" role="img" aria-label="Photo of a laundry room" style="left:0;top:108px;width:215px;height:366px;background:linear-gradient(180deg,#d9dde0,#b8bec3 60%,#8b9097)"></div>
  <div class="photo" role="img" aria-label="Photo of a bedroom" style="left:217px;top:108px;width:262px;height:180px;background:linear-gradient(180deg,#e5e6e9,#2e3f74)"></div>
  <div class="photo" role="img" aria-label="Photo of a terrace" style="left:217px;top:290px;width:262px;height:184px;background:linear-gradient(180deg,#8fa9b8,#a7463a 60%,#4a4a46)"></div>
  <div class="photo" role="img" aria-label="Photo of a pool with palm trees" style="left:481px;top:108px;width:240px;height:366px;background:linear-gradient(180deg,#c9dbe8,#5e7a4a 45%,#4aa4c4 80%,#9a9e9a)"></div>
  <div class="photo" role="img" aria-label="Photo of a kitchen" style="left:723px;top:108px;width:262px;height:180px;background:linear-gradient(180deg,#f1f2f3,#3e4245)"></div>
  <div class="photo" role="img" aria-label="Photo of a bathroom" style="left:723px;top:290px;width:262px;height:184px;background:linear-gradient(180deg,#e9ecee,#b9c0c4)"></div>
  <div class="photo" role="img" aria-label="Photo of a white hallway" style="left:987px;top:108px;width:213px;height:366px;background:linear-gradient(180deg,#f3f3f3,#c8cccf)"></div>
</section>

<section class="contact">
  <div class="photo map" role="img" aria-label="Street map showing the apartment location"></div>
  <div class="contact-form">
    <div class="field">Name</div>
    <div class="field">Email</div>
    <div class="field">Subject</div>
    <div class="field message">Message</div>
    <span class="submit">Submit</span>
  </div>
</section>

<footer class="footer">
  <div class="fcol" style="left:148px"><h4>Menu</h4><ul><li>Home</li><li>About us</li><li>Properties</li><li>Blog</li><li>Contact</li></ul></div>
  <div class="fcol" style="left:308px"><h4>Contact us</h4><p>12 Harbour Road, Baywater<br>120 Shore Lane</p><p>+000 1234 567 890</p><p>hello@harbourlane.test</p></div>
  <div class="fcol" style="left:540px"><h4>Photo Feed</h4>
    <div class="feed" role="img" aria-label="Small apartment photos">
      <span style="background:#9aa7ae"></span><span style="background:#c9ccd0"></span><span style="background:#7f8a72"></span>
      <span style="background:#b6b0a9"></span><span style="background:#d3d6d8"></span><span style="background:#8f9aa1"></span>
    </div></div>
  <div class="fcol" style="left:852px;width:260px"><h4 style="margin-bottom:8px">About Us</h4><p style="line-height:1.5">Seaside apartments for short and long stays, booked direct with the owners.</p>
    <h4 style="margin:12px 0 0">Newsletter</h4>
    <div class="news-form"><span>Enter your email</span><b>Subscribe</b></div></div>
  <div class="footer-brand"><span class="dot"></span>HARBOURLANE</div>
  <p class="copyright">Copyright © 2019 <b>Harbourlane</b>. All rights reserved.</p>
</footer>

</body>
</html>
```